Price Trend Graphic for Estimates

I want to add a graphic to my estimates that shows the projected price trend of the work we are quoting to the customer. I have attached a couple ideas I was working on but they are garbage. Hopefully you can see the intent and make it look a lot better. Basically I want the customer to see a really a professional / technological graphic that will stimulate them to purchase Right Now! before the price goes up further. So maybe if the "Today's Price" looks nice and friendly and then becomes more critical and ominous as it goes forward 30 days.... 90 days.... Idea is to psychologically

Target Market(s)

Customers for our Construction business

Industry/Entity Type

Construction

Colors
0054AA
0677BA
7BADD7
CADEEF
E8F1F8
0094D4
00A9DD
6FCCEA
C7EBF8
E9F6FB
FFF300
FFF600
FEFA6F
FFFEC7
FFFEE8
F0912C
F2A743
F7CA91
FBE8D2
FDF5EE

Requirements
Must have
• nice looking graphic with upwards moving arrow and 3 price points
Nice to have
• technological / modern looking chart

```html
<!DOCTYPE html>
<html lang="en">
<head>
<meta charset="utf-8">
<title>Price Trend Estimate Graphic</title>
<link href="https://fonts.googleapis.com/css2?family=Lato:ital,wght@0,400;0,700;0,900;1,400&family=Montserrat:ital,wght@1,800&family=Roboto+Condensed:wght@700&display=swap" rel="stylesheet">
<style>
  :root {
    --stage: #2b2b2b;
    --navy: #0054AA;
    --navy-deep: #0a2150;
    --sky: #00A9DD;
    --sky-light: #6FCCEA;
    --yellow: #FFF300;
    --yellow-edge: #d9cf00;
    --violet: #6b63d8;
    --ink: #111;
    --label: #0a3d7a;
  }
  * { margin: 0; padding: 0; box-sizing: border-box; }
  html, body { width: 1200px; height: 1177px; overflow: hidden; background: var(--stage); }
  .flyer {
    position: absolute; left: 254px; top: 115px; width: 726px; height: 939px;
    background: linear-gradient(100deg, var(--violet) 0%, #5a7fdc 55%, #4a9be4 100%);
    overflow: hidden; font-family: "Lato", sans-serif;
  }
  .tech-backdrop {
    position: absolute; right: 0; top: 0; width: 170px; height: 877px;
    background: linear-gradient(90deg, rgba(74,155,228,0) 0%, rgba(120,190,240,0.55) 55%, rgba(150,205,245,0.75) 100%);
  }
  .panel {
    position: absolute; left: 90px; width: 596px; height: 254px;
    background: linear-gradient(90deg, #ebe9f8 0%, #eef1fb 60%, rgba(232,241,252,0.92) 100%);
  }
  .panel svg { position: absolute; left: 0; top: 0; width: 596px; height: 254px; }
  .price { font-family: "Roboto Condensed", sans-serif; font-weight: 700; font-size: 15px; fill: var(--ink); text-anchor: middle; }
  .tick { font-family: "Lato", sans-serif; font-weight: 900; font-size: 11.5px; fill: var(--label); text-anchor: middle; }
  .pill {
    position: absolute; left: 0; width: 172px; height: 190px;
    border-radius: 0 95px 95px 0;
    box-shadow: 0 0 0 9px rgba(200,215,245,0.75);
    display: flex; flex-direction: column; justify-content: center; padding-left: 14px;
  }
  .pill--signup { background: var(--navy); color: #fff; font-size: 24px; line-height: 1.08; }
  .pill--signup .lead { color: var(--yellow); font-weight: 900; }
  .pill--trend { background: var(--sky); color: var(--navy-deep); font-size: 34px; line-height: 1; padding-top: 62px; }
  .pill--trend strong { font-size: 35px; }
  .pill--estimate { background: var(--navy); color: var(--sky-light); font-size: 25px; line-height: 1; padding-top: 66px; }
  .pill--estimate strong { font-size: 38px; }
  .pill strong { font-weight: 900; }
  .tag-icon { position: absolute; left: 30px; top: 22px; width: 62px; height: 62px; }
  .credit { position: absolute; left: 6px; top: 864px; font-size: 9px; font-style: italic; color: #e6ecff; }
  .footer {
    position: absolute; left: 0; top: 877px; width: 726px; height: 62px;
    background: var(--navy-deep); color: #fff;
    display: flex; align-items: center; justify-content: center;
    font-family: "Montserrat", sans-serif; font-weight: 800; font-style: italic; font-size: 26px;
  }
  .footer em { color: var(--yellow); font-style: italic; }
</style>
</head>
<body>
<main class="flyer">
  <div class="tech-backdrop" role="img" aria-label="Decorative connected-network pattern in white on light blue"></div>

  <!-- Row 1 -->
  <section class="panel" style="top:39px">
    <svg viewBox="0 0 596 254" aria-label="Price rises from $6,500 today to $7,460 at 90 days">
      <g stroke="#8aa0d8" stroke-dasharray="2 3" stroke-width="1">
        <line x1="167" y1="179" x2="167" y2="209"/><line x1="282" y1="161" x2="282" y2="209"/><line x1="520" y1="134" x2="520" y2="209"/>
      </g>
      <polyline points="167,179 282,161 520,134 576,107" fill="none" stroke="#7f86dc" stroke-width="2"/>
      <polygon points="584,102 566,104 574,116" fill="#6a6fd6"/>
      <circle cx="167" cy="179" r="3.5" fill="var(--navy)"/><circle cx="282" cy="161" r="3.5" fill="var(--sky)"/><circle cx="520" cy="134" r="3.5" fill="var(--yellow-edge)"/>
      <rect x="158" y="203" width="378" height="14" rx="7" fill="#fff"/>
      <rect x="162" y="205" width="122" height="10" fill="var(--navy)"/>
      <rect x="284" y="205" width="122" height="10" fill="var(--sky)"/>
      <rect x="406" y="205" width="124" height="10" fill="var(--yellow)"/>
      <g><circle cx="163" cy="130" r="42" fill="#fff" stroke="var(--navy)" stroke-width="1.5"/><circle cx="163" cy="130" r="34" fill="#fff" stroke="var(--navy)" stroke-width="5"/><text class="price" x="163" y="135">$ 6,500</text></g>
      <g><circle cx="278" cy="108" r="42" fill="#fff" stroke="var(--sky)" stroke-width="1.5"/><circle cx="278" cy="108" r="34" fill="#fff" stroke="var(--sky)" stroke-width="5"/><text class="price" x="278" y="113">$ 7,280</text></g>
      <g><circle cx="506" cy="78" r="42" fill="#fff" stroke="var(--yellow-edge)" stroke-width="1.5"/><circle cx="506" cy="78" r="34" fill="#fff" stroke="var(--yellow)" stroke-width="5"/><text class="price" x="506" y="83">$ 7,460</text></g>
      <text class="tick" x="168" y="236">TODAY</text><text class="tick" x="276" y="236">30 DAYS</text>
      <text class="tick" x="402" y="236">60 DAYS</text><text class="tick" x="520" y="236">90 DAYS</text>
    </svg>
  </section>
  <div class="pill pill--signup" style="top:71px">
    <span class="lead">SIGN UP</span><span class="lead">TODAY</span><span>FOR HUGE</span><span>SAVINGS!</span>
  </div>

  <!-- Row 2 -->
  <section class="panel" style="top:313px">
    <svg viewBox="0 0 596 254" aria-label="Price trend from $6,500 today to $7,460 at 60 days">
      <g stroke="#8aa0d8" stroke-dasharray="2 3" stroke-width="1">
        <line x1="167" y1="179" x2="167" y2="208"/><line x1="282" y1="160" x2="282" y2="208"/><line x1="403" y1="132" x2="403" y2="208"/>
      </g>
      <polyline points="167,179 282,160 403,132 520,84" fill="none" stroke="#7f86dc" stroke-width="2"/>
      <polygon points="528,80 510,80 516,93" fill="#6a6fd6"/>
      <circle cx="167" cy="179" r="3.5" fill="var(--navy)"/><circle cx="282" cy="160" r="3.5" fill="var(--sky)"/><circle cx="403" cy="132" r="3.5" fill="var(--yellow-edge)"/>
      <rect x="158" y="202" width="378" height="14" rx="7" fill="#fff"/>
      <rect x="162" y="204" width="122" height="10" fill="var(--navy)"/>
      <rect x="284" y="204" width="122" height="10" fill="var(--sky)"/>
      <rect x="406" y="204" width="124" height="10" fill="var(--yellow)"/>
      <g><circle cx="163" cy="127" r="42" fill="#fff" stroke="var(--navy)" stroke-width="1.5"/><circle cx="163" cy="127" r="34" fill="#fff" stroke="var(--navy)" stroke-width="5"/><text class="price" x="163" y="132">$ 6,500</text></g>
      <g><circle cx="278" cy="106" r="42" fill="#fff" stroke="var(--sky)" stroke-width="1.5"/><circle cx="278" cy="106" r="34" fill="#fff" stroke="var(--sky)" stroke-width="5"/><text class="price" x="278" y="111">$ 7,280</text></g>
      <g><circle cx="397" cy="80" r="42" fill="#fff" stroke="var(--yellow-edge)" stroke-width="1.5"/><circle cx="397" cy="80" r="34" fill="#fff" stroke="var(--yellow)" stroke-width="5"/><text class="price" x="397" y="85">$ 7,460</text></g>
      <text class="tick" x="168" y="233">TODAY</text><text class="tick" x="276" y="233">30 DAYS</text>
      <text class="tick" x="402" y="233">60 DAYS</text><text class="tick" x="520" y="235">90 DAYS</text>
    </svg>
  </section>
  <div class="pill pill--trend" style="top:347px">
    <svg class="tag-icon" viewBox="0 0 46 46" aria-hidden="true">
      <path d="M6 20 L22 6 L38 8 L40 24 L24 40 Z" fill="#fff" transform="rotate(-8 23 23)"/>
      <circle cx="32" cy="14" r="3" fill="var(--sky)"/>
      <path d="M32 14 C38 4 46 6 42 14" stroke="#fff" stroke-width="2" fill="none"/>
      <text x="20" y="30" font-family="Lato, sans-serif" font-weight="900" font-size="17" fill="var(--sky)" text-anchor="middle">$</text>
    </svg>
    <span>PRICE</span><strong>TREND</strong>
  </div>

  <!-- Row 3 -->
  <section class="panel" style="top:588px">
    <svg viewBox="0 0 596 254" aria-label="Estimated price from $6,500 to $7,460 over 60 days">
      <g stroke="#8aa0d8" stroke-dasharray="2 3" stroke-width="1">
        <line x1="167" y1="179" x2="167" y2="208"/><line x1="282" y1="160" x2="282" y2="208"/><line x1="403" y1="132" x2="403" y2="208"/>
      </g>
      <polyline points="167,179 282,160 403,132 520,84" fill="none" stroke="#7f86dc" stroke-width="2"/>
      <polygon points="528,80 510,80 516,93" fill="#6a6fd6"/>
      <circle cx="167" cy="179" r="3.5" fill="var(--navy)"/><circle cx="282" cy="160" r="3.5" fill="var(--sky)"/><circle cx="403" cy="132" r="3.5" fill="var(--yellow-edge)"/>
      <rect x="158" y="202" width="378" height="14" rx="7" fill="#fff"/>
      <rect x="162" y="204" width="122" height="10" fill="var(--navy)"/>
      <rect x="284" y="204" width="122" height="10" fill="var(--sky)"/>
      <rect x="406" y="204" width="124" height="10" fill="var(--yellow)"/>
      <g><circle cx="163" cy="128" r="42" fill="#fff" stroke="var(--navy)" stroke-width="1.5"/><circle cx="163" cy="128" r="34" fill="#fff" stroke="var(--navy)" stroke-width="5"/><text class="price" x="163" y="133">$ 6,500</text></g>
      <g><circle cx="278" cy="106" r="42" fill="#fff" stroke="var(--sky)" stroke-width="1.5"/><circle cx="278" cy="106" r="34" fill="#fff" stroke="var(--sky)" stroke-width="5"/><text class="price" x="278" y="111">$ 7,280</text></g>
      <g><circle cx="397" cy="79" r="42" fill="#fff" stroke="var(--yellow-edge)" stroke-width="1.5"/><circle cx="397" cy="79" r="34" fill="#fff" stroke="var(--yellow)" stroke-width="5"/><text class="price" x="397" y="84">$ 7,460</text></g>
      <text class="tick" x="168" y="233">TODAY</text><text class="tick" x="276" y="233">30 DAYS</text>
      <text class="tick" x="402" y="233">60 DAYS</text><text class="tick" x="520" y="236">90 DAYS</text>
    </svg>
  </section>
  <div class="pill pill--estimate" style="top:620px">
    <svg class="tag-icon" viewBox="0 0 46 46" aria-hidden="true">
      <path d="M6 20 L22 6 L38 8 L40 24 L24 40 Z" fill="#fff" transform="rotate(-8 23 23)"/>
      <circle cx="32" cy="14" r="3" fill="var(--navy)"/>
      <path d="M32 14 C38 4 46 6 42 14" stroke="#fff" stroke-width="2" fill="none"/>
      <text x="20" y="30" font-family="Lato, sans-serif" font-weight="900" font-size="17" fill="var(--navy)" text-anchor="middle">$</text>
    </svg>
    <span>ESTIMATED</span><strong>PRICE</strong>
  </div>

  <p class="credit">Icon by Pixelmint from Iconyard.com</p>
  <footer class="footer"><span>Get Today’s <em>BEST DEAL</em>. Hurry Up!</span></footer>
</main>
</body>
</html>
```